Flyer für ein soziales Dienstleistungsunternehmen
Zielgruppe
Wir sind ein soziales Dienstleistungsunternehmen, welches versucht durch Workshops und Vorträge für Kinder, Jugendliche und deren Betreuungspersonen (auch Lehrkräfte, Erzieher/innen, Eltern, usw.) Prävention und Aufklärung bezüglich mentale Gesundheit zu betreiben und so auch Entstigmatisierung zu ermöglichen. Wir möchten einen allgemeinen Flyer erstellen, der für Schulen, Kindergärten und andere Einrichtungen, aber auch Eltern und Ämter interessant ist.
Aufgabenstellung
-vorhandenes Logo soll integriert werden, Farbe und Gestaltung daran anpassen
-Platz lassen für Slogan
-überschaubar, Überblick über unsere Angebote (Texte liefern wir selbst)
-ansprechend und Interesse weckend
-nicht 0815/Standard mentale Gesundheit-Flyer bitte :)
-modern, locker, dynamisch, jugendlich

```html
<!DOCTYPE html>
<html lang="de">
<head>
<meta charset="utf-8">
<title>Mental Health Matters – Flyer</title>
<link href="https://fonts.googleapis.com/css2?family=Caveat:wght@600&family=Kaushan+Script&family=Montserrat:wght@400;600;700&display=swap" rel="stylesheet">
<style>
  :root{
    --bg:#e1e4e6;
    --paper:#ffffff;
    --teal:#3f8b97;
    --teal-dark:#2f7380;
    --mint:#a8dbd1;
    --mint-light:#d4efe9;
    --ink:#484848;
    --ink-soft:#6a6a6a;
    --white:#ffffff;
  }
  *{margin:0;padding:0;box-sizing:border-box}
  html,body{width:1200px;height:900px;overflow:hidden;background:var(--bg)}
  body{font-family:"Montserrat",Arial,sans-serif;color:var(--ink);position:relative}
  .flyer{position:absolute;top:40px;width:400px;height:820px;background:var(--paper);overflow:hidden;box-shadow:0 6px 20px rgba(0,0,0,.12)}
  .flyer--front{left:170px}
  .flyer--back{left:630px}
  .wave{position:absolute;left:0;width:100%;display:block}
  .illustration{position:absolute;border-radius:50%;background:radial-gradient(circle at 45% 45%,var(--mint) 0%,var(--mint-light) 70%)}
  /* front */
  .quote{position:absolute;top:40px;left:36px;width:250px;font-family:"Caveat",cursive;font-size:22px;line-height:1.05;color:var(--teal)}
  .quote__author{display:block;font-family:"Montserrat",sans-serif;font-size:9px;color:var(--ink-soft);margin-top:4px}
  .front__illustration{top:120px;left:230px;width:150px;height:150px}
  .headline{position:absolute;top:160px;left:24px;width:360px;font-family:"Kaushan Script",cursive;font-size:74px;line-height:.95;color:var(--ink);transform:rotate(-8deg)}
  .headline span{display:block}
  .headline span:nth-child(2){padding-left:50px}
  .headline span:nth-child(3){padding-left:30px}
  .tagline{position:absolute;top:440px;right:28px;text-align:right;font-weight:700;font-size:19px;line-height:1.2;color:var(--ink)}
  .intro{position:absolute;top:510px;left:150px;width:220px;font-size:11px;line-height:1.5;color:var(--ink-soft)}
  .brand{position:absolute;top:636px;left:30px;width:100px;display:flex;flex-direction:column;align-items:center;gap:6px}
  .brand__dot{width:34px;height:34px;border-radius:50%;background:var(--mint)}
  .brand__name{font-size:16px;font-weight:600;color:var(--teal)}
  .contact{position:absolute;top:616px;left:150px;width:230px;font-size:10.5px;line-height:1.5;color:var(--ink-soft)}
  .contact strong{color:var(--ink);font-weight:700}
  .web{position:absolute;top:738px;right:30px;font-family:"Caveat",cursive;font-size:22px;color:var(--ink)}
  /* back */
  .vision-title{position:absolute;top:40px;left:30px;font-family:"Kaushan Script",cursive;font-size:58px;line-height:.9;color:var(--ink);transform:rotate(-6deg)}
  .vision-title span{display:block;padding-left:40px}
  .vision-text{position:absolute;top:70px;left:222px;width:150px;font-size:11px;line-height:1.45;color:var(--ink-soft);text-align:right}
  .offers{position:absolute;top:185px;left:30px;width:205px;font-size:11px;line-height:1.4;color:var(--ink-soft)}
  .offers h3{font-size:12.5px;font-weight:700;color:var(--ink);margin:10px 0 3px}
  .offers h3:first-child{margin-top:0}
  .offers ul{list-style:none}
  .offers li::before{content:"· ";color:var(--teal);font-weight:700}
  .back__illustration{top:310px;left:248px;width:132px;height:190px;border-radius:50% 50% 40% 40%}
  .cta{position:absolute;bottom:40px;left:30px;width:320px;color:var(--white);font-size:11px;line-height:1.5}
  .cta strong{display:block;font-size:12.5px;margin-top:8px}
</style>
</head>
<body>

<section class="flyer flyer--front">
  <svg class="wave" style="top:0" height="150" viewBox="0 0 400 150" preserveAspectRatio="none">
    <path d="M260 0 H400 V150 C380 90 330 40 260 0Z" fill="var(--mint)"/>
    <path d="M300 0 H400 V100 C380 55 350 20 300 0Z" fill="var(--teal)"/>
  </svg>
  <p class="quote">Was wir heute tun, entscheidet darüber, wie die Welt morgen aussieht<span class="quote__author">Maria Lindenau</span></p>
  <div class="illustration front__illustration" role="img" aria-label="Illustration: Person zwischen Blättern und Blüten"></div>
  <h1 class="headline"><span>Mental</span><span>Health</span><span>Matters</span></h1>
  <p class="tagline">– Prävention für eine<br>starke Generation!</p>
  <p class="intro">Die Mental Health Coaches bieten präventive Unterstützung und Aufklärung rund um das Thema mentale Gesundheit für Kinder, Jugendliche, deren Bezugspersonen und Fachpersonal.</p>
  <svg class="wave" style="bottom:0" height="260" viewBox="0 0 400 260" preserveAspectRatio="none">
    <path d="M0 40 C120 120 160 60 180 140 C200 220 320 200 400 160 V260 H0Z" fill="var(--mint-light)"/>
    <path d="M0 170 C60 150 100 200 0 230Z" fill="var(--mint)"/>
    <path d="M250 260 C300 200 360 190 400 170 V260Z" fill="var(--teal)"/>
  </svg>
  <div class="brand"><span class="brand__dot"></span><span class="brand__name">Seelenweg</span></div>
  <p class="contact"><strong>Seelenweg<br>L. Hartmann &amp; M. Brenner GbR</strong><br>Lindenstraße 12<br>86000 Musterstadt<br>Tel. 01234-567890<br>E-Mail: kontakt@seelenweg-beispiel.de</p>
  <p class="web">www.seelenweg-beispiel.de</p>
</section>

<section class="flyer flyer--back">
  <svg class="wave" style="top:0" height="140" viewBox="0 0 400 140" preserveAspectRatio="none">
    <path d="M220 0 H400 V140 C360 60 300 20 220 0Z" fill="var(--mint-light)"/>
    <path d="M300 0 H400 V80 C370 40 340 15 300 0Z" fill="var(--teal)"/>
  </svg>
  <h2 class="vision-title">Unsere<span>Vision</span></h2>
  <p class="vision-text">Prävention im Rahmen von persönlicher, sozialer und emotionaler Entwicklung als fest integrierten Bestandteil im Alltag von Kindern und Jugendlichen bringen.</p>
  <div class="offers">
    <h3>Unsere Ziele</h3>
    <ul><li>Aufklärung und Information</li><li>Entstigmatisierung</li><li>Stärkung</li></ul>
    <h3>Was bieten wir?</h3>
    <ul><li>Informationsveranstaltungen</li><li>Vorträge</li><li>Workshops</li><li>u.v.m.</li></ul>
    <h3>An wen richtet sich unser Angebot?</h3>
    <ul><li>Kinder und Jugendliche</li><li>Eltern und andere Bezugspersonen</li><li>Fachpersonal (Lehrkräfte, Pädagogisches Personal usw.)</li><li>Einrichtungen (Schule, Kindergarten usw.)</li></ul>
    <h3>In welchem Rahmen können wir unterstützen?</h3>
    <ul><li>Fortbildungen</li><li>Projekttage</li><li>Elternabende</li><li>u.v.m.</li></ul>
  </div>
  <div class="illustration back__illustration" role="img" aria-label="Illustration: Kopf im Profil mit Puzzleteilen und einer Person"></div>
  <svg class="wave" style="bottom:0" height="230" viewBox="0 0 400 230" preserveAspectRatio="none">
    <path d="M0 60 C120 20 260 80 400 20 V230 H0Z" fill="var(--mint)"/>
    <path d="M0 90 C140 50 260 110 400 50 V230 H0Z" fill="var(--teal)"/>
  </svg>
  <p class="cta">Unsere Angebote sind vielfältig und individuell an Ihren Bedarf angepasst.<strong>Vereinbaren Sie ein kostenloses Erstgespräch und erfahren Sie mehr über unsere Angebote!</strong></p>
</section>

</body>
</html>
```